Talent Management Company Needs Business Cards

Using one of the logos provided (attached) K&K Talent Collective needs a business card designed.
Please visit our website for more information about us-

www.kktalentcollective.net

The face should feature a dramatic presentation of the logo with the back being reserved for our professional information which is:

The information should be:
Darnell T. Fosbury
C.E.O
Email: dtfosbury@kktalentcollective.net
Mobile: 216-555-0193
Website: www.kktalentcollective.net

Marcus L. Fosbury
Director of Public Relations
Email: mlfosbury@kktalentcollective.net
Mobile: 216-555-0147

Rory J. Whitcomb
Director of Client Development
Email: rwhitcomb@kktalentcollective.net

Glenn Strauss
Director of Brand Development
Email: gstrauss@kktalentcollective.net

Would like the logo to have color. I would like to see one side red or black and the other side white but if it looks better in either black or red that would be fine to but would like to see how it comes out.

Please feel free to message me and if you would like just the icon alone I have other image files that I can send as well.

Target Market(s)

Professional Athletes, coaches, entertainers age 18-35 but also must be accepted in the business community

Industry/Entity Type

Business

Requirements
Must have
• 1) Use the logo
2) Double sided
3) Distinctive
Nice to have
• Small simple images for telephone, e-mail, and Url.

```html
<!DOCTYPE html>
<html lang="en">
<head>
<meta charset="utf-8">
<title>K&amp;K Talent Collective — Business Card</title>
<link rel="stylesheet" href="https://fonts.googleapis.com/css2?family=Jost:ital,wght@0,400;0,500;1,400&display=swap">
<style>
  :root {
    --page: #ffffff;
    --ink: #111111;
    --ink-soft: #3a3a3a;
    --ink-muted: #555555;
    --accent: #e0232e;
    --card-edge: #8a8a8a;
    --front-dark: #0b0b0b;
    --front-mid: #2a2a2a;
  }
  html, body {
    margin: 0;
    padding: 0;
    width: 1200px;
    height: 926px;
    overflow: hidden;
    background: var(--page);
  }
  .canvas {
    position: relative;
    width: 1200px;
    height: 926px;
    font-family: "Jost", sans-serif;
    color: var(--ink);
  }
  .card {
    position: absolute;
    top: 97px;
    width: 472px;
    height: 730px;
    box-sizing: border-box;
  }
  .card--front {
    left: 116px;
    background: radial-gradient(ellipse at 60% 40%, var(--front-mid) 0%, var(--front-dark) 75%);
  }
  .front-pattern {
    position: absolute;
    inset: 0;
    background: linear-gradient(180deg, rgba(255,255,255,0.04) 0%, rgba(255,255,255,0) 60%);
  }
  .front-brand {
    position: absolute;
    top: 150px;
    right: 48px;
    display: flex;
    align-items: center;
    gap: 14px;
  }
  .front-brand__mark {
    width: 30px;
    height: 30px;
    background: var(--accent);
  }
  .front-brand__name {
    font-weight: 500;
    font-size: 26px;
    line-height: 1.1;
    color: #ffffff;
    letter-spacing: 0.5px;
  }
  .card--back {
    left: 624px;
    background: #ffffff;
    border: 1.5px solid var(--card-edge);
  }
  .back-brand {
    position: absolute;
    top: 130px;
    left: 52px;
    right: 40px;
    display: flex;
    flex-direction: column;
    align-items: center;
    gap: 36px;
  }
  .back-brand__mark {
    width: 62px;
    height: 62px;
    background: var(--accent);
  }
  .back-brand__name {
    font-weight: 500;
    font-size: 29px;
    letter-spacing: 0.3px;
    text-transform: uppercase;
    color: var(--ink);
    white-space: nowrap;
  }
  .person {
    position: absolute;
    left: 53px;
    top: 385px;
  }
  .person__name {
    margin: 0;
    font-weight: 500;
    font-size: 22px;
    color: var(--ink-soft);
    letter-spacing: 0.4px;
  }
  .person__title {
    margin: 2px 0 0;
    font-style: italic;
    font-size: 22px;
    color: var(--ink-soft);
  }
  .contact {
    position: absolute;
    left: 53px;
    top: 482px;
    margin: 0;
    padding: 0;
    list-style: none;
    font-size: 19px;
    line-height: 27px;
    color: var(--ink-muted);
  }
  .contact__label {
    display: inline-block;
    width: 24px;
    font-weight: 500;
    color: var(--accent);
  }
  .address {
    position: absolute;
    left: 53px;
    top: 600px;
    margin: 0;
    font-style: normal;
    font-size: 19px;
    line-height: 25px;
    color: var(--ink-muted);
  }
  .side-label {
    position: absolute;
    top: 842px;
    width: 472px;
    text-align: center;
    font-size: 34px;
    font-weight: 400;
    color: var(--ink);
  }
  .side-label--front { left: 116px; }
  .side-label--back { left: 624px; }
</style>
</head>
<body>
<main class="canvas">
  <section class="card card--front">
    <div class="front-pattern" role="img" aria-label="Dark background with a faint repeating pattern of the brand symbol"></div>
    <div class="front-brand">
      <span class="front-brand__mark"></span>
      <span class="front-brand__name">K&amp;K Talent<br>Collective</span>
    </div>
  </section>

  <section class="card card--back">
    <div class="back-brand">
      <span class="back-brand__mark"></span>
      <span class="back-brand__name">K&amp;K Talent Collective</span>
    </div>

    <div class="person">
      <p class="person__name">Darnell T. Fosbury</p>
      <p class="person__title">CEO</p>
    </div>

    <ul class="contact">
      <li><span class="contact__label">T :</span> 216-555-0193</li>
      <li><span class="contact__label">E :</span> dtfosbury@kktalentcollective.net</li>
      <li><span class="contact__label">W:</span> www.kktalentcollective.net</li>
    </ul>

    <address class="address">
      2715 Marlowe Crossing Rd<br>
      Suite 410, Halvern Park, OH 45090
    </address>
  </section>

  <div class="side-label side-label--front">Front</div>
  <div class="side-label side-label--back">Back</div>
</main>
</body>
</html>
```